Eastfield Commercial Card

I would like a modern, eye catching card based off my logo design.
Info to include:
Anders Voll (Card Name)
eastfieldcommercial.example (Website)
555 203 8841 (Office/fax)
555 287 3096 (Business Cell)
anders@eastfieldcommercial.example (Work email)

Target Market(s)

Commercial real estate brokers, property owners.

Colors
ec1f27
757575

Requirements
Must have
• Name and info above. Not be lame!:)

```html
<!DOCTYPE html>
<html lang="en">
<head>
<meta charset="utf-8">
<title>Eastfield Commercial Card</title>
<link rel="stylesheet" href="https://fonts.googleapis.com/css2?family=Cinzel:wght@400&family=Lato:wght@400&family=Montserrat:wght@700&display=swap">
<style>
  :root {
    --brand-red: #ec1f27;
    --brand-gray: #757575;
    --gray-dark: #6e6e6e;
    --gray-light: #858585;
    --paper: #ffffff;
    --blush: #f6eeee;
    --backdrop: #8a8a8a;
  }
  html, body {
    margin: 0;
    width: 1200px;
    height: 1200px;
    overflow: hidden;
    background: var(--backdrop);
  }
  .sheet {
    width: 1200px;
    height: 1200px;
    display: flex;
    flex-direction: column;
    align-items: center;
    justify-content: center;
    gap: 60px;
  }
  .card {
    position: relative;
    width: 900px;
    height: 514px;
    overflow: hidden;
    box-shadow: 0 10px 30px rgba(0,0,0,0.25);
  }
  .card-front { background: var(--paper); }
  .card-back { background: var(--brand-gray); }

  .front-texture {
    position: absolute;
    inset: 0;
    background: radial-gradient(circle at 33% 39%, var(--blush) 0%, var(--blush) 18%, var(--paper) 55%);
  }
  .back-texture {
    position: absolute;
    inset: 0;
    background: linear-gradient(135deg, var(--gray-light) 0%, var(--brand-gray) 50%, var(--gray-dark) 100%);
  }
  .front-bands {
    position: absolute;
    inset: 0;
    width: 100%;
    height: 100%;
  }

  .wordmark {
    position: absolute;
    display: flex;
    align-items: center;
    gap: 14px;
    font-family: "Montserrat", sans-serif;
    font-weight: 700;
    letter-spacing: 1px;
    text-transform: uppercase;
    white-space: nowrap;
  }
  .wordmark-mark {
    width: 22px;
    height: 22px;
    flex: none;
  }
  .card-front .wordmark {
    left: 70px;
    top: 120px;
    font-size: 28px;
    color: var(--brand-red);
  }
  .card-front .wordmark-mark { background: var(--brand-red); }

  .holder {
    position: absolute;
    left: 500px;
    top: 300px;
    color: var(--paper);
  }
  .holder-name {
    font-family: "Cinzel", serif;
    font-weight: 400;
    font-size: 44px;
    letter-spacing: 2px;
    margin: 0 0 18px;
    padding-bottom: 6px;
    border-bottom: 2px solid var(--paper);
    display: inline-block;
    text-transform: uppercase;
  }
  .contact-list {
    list-style: none;
    margin: 0;
    padding: 0;
    font-family: "Lato", sans-serif;
    font-size: 20px;
    line-height: 30px;
  }
  .contact-list li {
    display: flex;
    align-items: center;
    gap: 10px;
    white-space: nowrap;
  }
  .contact-list svg {
    width: 16px;
    height: 16px;
    fill: var(--paper);
    flex: none;
  }

  .back-lockup {
    position: absolute;
    left: 0;
    right: 0;
    top: 170px;
    display: flex;
    flex-direction: column;
    align-items: center;
    color: var(--paper);
  }
  .card-back .wordmark {
    position: static;
    font-size: 34px;
    color: var(--paper);
    padding: 18px 10px;
    border-top: 2px solid var(--paper);
    border-bottom: 2px solid var(--paper);
  }
  .card-back .wordmark-mark { background: var(--paper); }
  .back-url {
    font-family: "Lato", sans-serif;
    font-size: 22px;
    margin-top: 16px;
    padding-bottom: 12px;
    border-bottom: 2px solid var(--paper);
    letter-spacing: 0.5px;
  }
</style>
</head>
<body>
<main class="sheet">

  <section class="card card-front" aria-label="Card front">
    <div class="front-texture" role="img" aria-label="Soft pale pink light rays behind the company name"></div>
    <svg class="front-bands" viewBox="0 0 900 514" preserveAspectRatio="none" aria-hidden="true">
      <polygon points="280,514 445,210 900,255 900,292 465,248 330,514" fill="var(--brand-red)"/>
      <polygon points="330,514 465,248 900,292 900,514" fill="var(--brand-gray)"/>
    </svg>

    <div class="wordmark">
      <span class="wordmark-mark"></span>
      <span>Eastfield Commercial</span>
    </div>

    <div class="holder">
      <h1 class="holder-name">Anders Voll</h1>
      <ul class="contact-list">
        <li>
          <svg viewBox="0 0 24 24"><path d="M6.6 10.8a15 15 0 0 0 6.6 6.6l2.2-2.2a1 1 0 0 1 1-.25 11.4 11.4 0 0 0 3.6.57 1 1 0 0 1 1 1V20a1 1 0 0 1-1 1A17 17 0 0 1 3 4a1 1 0 0 1 1-1h3.5a1 1 0 0 1 1 1c0 1.25.2 2.45.57 3.57a1 1 0 0 1-.25 1z"/></svg>
          <span>555 203 8841</span>
        </li>
        <li>
          <svg viewBox="0 0 24 24"><path d="M7 1h10a2 2 0 0 1 2 2v18a2 2 0 0 1-2 2H7a2 2 0 0 1-2-2V3a2 2 0 0 1 2-2zm0 3v14h10V4zm5 15.5a1 1 0 1 0 0 2 1 1 0 0 0 0-2z"/></svg>
          <span>555 287 3096</span>
        </li>
        <li>
          <svg viewBox="0 0 24 24"><path d="M2 11 22 3l-8 20-3-9z"/></svg>
          <span>anders@eastfieldcommercial.example</span>
        </li>
        <li>
          <svg viewBox="0 0 24 24"><path d="M10.6 13.4a1 1 0 0 1 0-1.4l3.5-3.5a3 3 0 1 1 4.2 4.2l-2 2-1.4-1.4 2-2a1 1 0 0 0-1.4-1.4L12 13.4a1 1 0 0 1-1.4 0zM13.4 10.6a1 1 0 0 1 0 1.4l-3.5 3.5a3 3 0 1 1-4.2-4.2l2-2 1.4 1.4-2 2a1 1 0 0 0 1.4 1.4L12 10.6a1 1 0 0 1 1.4 0z"/></svg>
          <span>eastfieldcommercial.example</span>
        </li>
      </ul>
    </div>
  </section>

  <section class="card card-back" aria-label="Card back">
    <div class="back-texture" role="img" aria-label="Faceted grey geometric background"></div>

    <div class="back-lockup">
      <div class="wordmark">
        <span class="wordmark-mark"></span>
        <span>Eastfield Commercial</span>
      </div>
      <div class="back-url">www.eastfieldcommercial.example</div>
    </div>
  </section>

</main>
</body>
</html>
```